Business card, rack card, & stationery for an educational speech therapy company
Voice Harbor
Professional
Lorna Pitchley
47915 Heron Street S Brookvale, MN 55990
lorna@voiceharborlearning.example
www.voiceharborlearning.example
Please provide an Illustrator file--if not available, a layered PSD file.
large logo and web address
voiceharbor voiceharbor
Pixelforge, this is not a logo project. this is a business stationary and brochure project.
Brightmark. You have a nice design but this is not a logo project. This is for business stationary and a brochure.
tidalfox tidalfox
Tidalfox. Very nice presentation with 171. We very much like the presentation with just the business card and Rack card as these two components are our main priority. They are very well coordinated. Thank you.
There have only been 3 rack card concepts proposed. We need more rack card submissions. There are two nice concepts but both need some improvements if the are going to win this competition.
Quorvantix. We really like designs 125 & 151. Please submit coordinating designs for the letterhead, envelope, and rack card. Thank you.
Please keep in mind that this project is for the following: A business card, letterhead, envelope, and a two sided 4" x 9" rack card (brochure)

```html
<!DOCTYPE html>
<html lang="en">
<head>
<meta charset="UTF-8">
<title>Voice Harbor Business Card</title>
<link href="https://fonts.googleapis.com/css2?family=Open+Sans:wght@400;600;700&family=Oswald:wght@500&display=swap" rel="stylesheet">
<style>
  :root {
    --stage: #e7e4df;
    --card: #ffffff;
    --ink: #4a4a4a;
    --ink-soft: #7a7a7a;
    --rule: #c9c9c9;
    --orange: #f39a1e;
    --green: #8cc63f;
    --green-light: #c6e59a;
    --mark: #4d4f52;
  }
  * { box-sizing: border-box; margin: 0; padding: 0; }
  html, body {
    width: 1200px; height: 914px; overflow: hidden;
    background: var(--stage);
  }
  .stage {
    position: relative; width: 1200px; height: 914px;
    display: flex; align-items: center; justify-content: center; gap: 40px;
  }
  .card {
    position: relative; width: 540px; height: 309px;
    background: var(--card);
    box-shadow: 0 6px 18px rgba(0,0,0,0.12);
    overflow: hidden;
  }

  /* Front */
  .brand {
    position: absolute; left: 30px; top: 34px;
    display: flex; align-items: center; gap: 10px;
  }
  .brand-dot {
    width: 38px; height: 38px; border-radius: 50%; background: var(--mark); flex: none;
  }
  .brand-text { display: flex; flex-direction: column; }
  .brand-name {
    font-family: 'Open Sans', sans-serif; font-weight: 700;
    font-size: 17px; line-height: 20px; color: var(--green); text-transform: uppercase;
    letter-spacing: 0.5px;
  }
  .brand-tagline {
    font-family: 'Open Sans', sans-serif; font-weight: 400;
    font-size: 10px; line-height: 13px; color: var(--ink-soft);
  }
  .holder-name {
    position: absolute; right: 30px; top: 40px;
    font-family: 'Oswald', sans-serif; font-weight: 500;
    font-size: 20px; color: var(--orange); letter-spacing: 0.5px;
    text-transform: uppercase;
  }
  .header-rule {
    position: absolute; left: 30px; right: 30px; top: 86px;
    height: 1px; background: var(--rule);
  }
  .swoosh { position: absolute; left: 0; top: 110px; width: 540px; height: 70px; }
  .contacts {
    position: absolute; left: 42px; top: 190px; list-style: none;
    font-family: 'Open Sans', sans-serif; font-size: 13px; color: var(--ink);
    line-height: 22px;
  }
  .contacts li { display: flex; align-items: center; gap: 10px; white-space: nowrap; }
  .contacts li::before {
    content: ""; width: 7px; height: 7px; background: var(--orange); flex: none;
  }

  /* Back */
  .back-mark {
    position: absolute; left: 0; right: 0; top: 62px;
    display: flex; flex-direction: column; align-items: center; gap: 12px;
  }
  .back-dot {
    width: 96px; height: 96px; border-radius: 50%; background: var(--mark);
  }
  .back-name {
    font-family: 'Open Sans', sans-serif; font-weight: 700;
    font-size: 16px; color: var(--green); text-transform: uppercase; letter-spacing: 0.5px;
  }
  .web-address {
    position: absolute; left: 0; right: 0; top: 232px; text-align: center;
    font-family: 'Open Sans', sans-serif; font-weight: 600;
    font-size: 16px; color: var(--green);
  }
</style>
</head>
<body>
<main class="stage">
  <section class="card card-front">
    <div class="brand">
      <span class="brand-dot"></span>
      <span class="brand-text">
        <span class="brand-name">Voice Harbor</span>
        <span class="brand-tagline">online speech therapy</span>
      </span>
    </div>
    <div class="holder-name">Lorna Pitchley</div>
    <div class="header-rule"></div>
    <svg class="swoosh" viewBox="0 0 540 70" aria-hidden="true">
      <defs>
        <linearGradient id="swooshFill" x1="0" y1="0" x2="1" y2="0">
          <stop offset="0" stop-color="#c6e59a"/>
          <stop offset="0.5" stop-color="#8cc63f"/>
          <stop offset="1" stop-color="#8cc63f"/>
        </linearGradient>
      </defs>
      <path d="M0 62 C150 40 330 28 540 4 L540 22 C350 44 170 56 0 70 Z" fill="url(#swooshFill)"/>
      <path d="M0 56 C180 36 360 22 540 0 L540 4 C340 28 160 44 0 60 Z" fill="#c6e59a" opacity="0.7"/>
    </svg>
    <ul class="contacts">
      <li>507-555-0148</li>
      <li>lorna@voiceharborlearning.example</li>
      <li>www.voiceharborlearning.example</li>
      <li>47915 Heron Street S Brookvale, MN 55990</li>
    </ul>
  </section>

  <section class="card card-back">
    <div class="back-mark">
      <span class="back-dot"></span>
      <span class="back-name">Voice Harbor</span>
    </div>
    <div class="web-address">www.voiceharborlearning.example</div>
  </section>
</main>
</body>
</html>
```